Business Card Design

Harbor Refuse 342 is a waste collection business contracted to remove waste from city streets, parks and caravan parks.

Target Market(s)

CEO and Managing Directors

Industry/Entity Type

Business

Contact Information for Business Card

Harbor Refuse 342
Manager
Dale Pickett
0439516204
harborrefuse342@quillmail.com.au

Colors
33a6d7
ecf7fb

Requirements
Must have
• Must have eye catching design that stands out above others ( tender process can be very competitive ).
Nice to have
• A garbage truck on or in the logo somehow

```html
<!DOCTYPE html>
<html lang="en">
<head>
<meta charset="utf-8">
<title>Harbor Refuse 342 — Business Card</title>
<link rel="stylesheet" href="https://fonts.googleapis.com/css2?family=Russo+One&family=Oswald:wght@300;400&family=Open+Sans:wght@300&display=swap">
<style>
  :root {
    --stage: #4a3338;
    --card-white: #ffffff;
    --card-black: #000000;
    --ink: #1a1a1a;
    --ink-soft: #3a3a3a;
  }
  * { margin: 0; padding: 0; box-sizing: border-box; }
  html, body {
    width: 1200px;
    height: 800px;
    overflow: hidden;
    background: var(--stage);
  }
  .canvas {
    position: relative;
    width: 1200px;
    height: 800px;
    display: flex;
    align-items: center;
    justify-content: center;
  }
  .card {
    position: relative;
    width: 900px;
    height: 520px;
    display: flex;
    box-shadow: 0 20px 50px rgba(0,0,0,0.35);
  }
  .card__info {
    position: relative;
    width: 470px;
    height: 100%;
    background: var(--card-white);
  }
  .card__brand {
    position: relative;
    flex: 1;
    height: 100%;
    background: var(--card-black);
  }
  .person-name {
    position: absolute;
    left: 150px;
    top: 150px;
    font-family: "Russo One", sans-serif;
    font-size: 38px;
    letter-spacing: 3px;
    text-transform: uppercase;
    color: var(--ink);
    white-space: nowrap;
  }
  .person-role {
    position: absolute;
    left: 250px;
    top: 210px;
    font-family: "Open Sans", sans-serif;
    font-weight: 300;
    font-size: 30px;
    color: var(--ink-soft);
  }
  .contact {
    position: absolute;
    left: 50px;
    top: 265px;
    font-family: "Oswald", sans-serif;
    font-weight: 300;
    font-size: 24px;
    line-height: 1.45;
    color: var(--ink-soft);
    list-style: none;
  }
  .brand-mark {
    position: absolute;
    right: 40px;
    top: 150px;
    width: 170px;
    height: 170px;
    border-radius: 50%;
    background: var(--card-white);
    display: flex;
    align-items: center;
    justify-content: center;
    text-align: center;
  }
  .brand-mark__name {
    font-family: "Oswald", sans-serif;
    font-weight: 300;
    font-size: 24px;
    line-height: 1.15;
    color: var(--ink);
    padding: 0 18px;
  }
</style>
</head>
<body>
  <main class="canvas">
    <article class="card">
      <section class="card__info">
        <h1 class="person-name">Dale Pickett</h1>
        <p class="person-role">Manager</p>
        <ul class="contact">
          <li class="contact__company">Harbor Refuse 342</li>
          <li class="contact__phone">0439516204</li>
        </ul>
      </section>
      <section class="card__brand">
        <div class="brand-mark">
          <span class="brand-mark__name">Harbor Refuse 342</span>
        </div>
      </section>
    </article>
  </main>
</body>
</html>
```